Company Information Flyer

I am looking for a Flyer / Brochure that we will hand out to new customers and will tell them who we are, what we offer and what we can do for them. Our company is called Brightvale Parts & Supply Company. We are a supplier of Original parts for the automotive industry. We are an Torvane (Halbrook Vehicles) Distributor. I would like to closely follow the information contained in the kestrelparts.com site. The information contained in the kestrelparts.com site explains the importance of using original or genuine parts and the advantages it provides. We would like to incorporate this information into our Brightvale Parts & Supply Company. Thank you.

```html
<!DOCTYPE html>
<html lang="en">
<head>
<meta charset="utf-8">
<title>Brightvale Parts &amp; Supply Company – Flyer</title>
<link href="https://fonts.googleapis.com/css2?family=Anton&family=Oswald:wght@600;700&family=Arimo:wght@400;700&display=swap" rel="stylesheet">
<style>
  :root {
    --bg: #2f3133;
    --paper: #f7f7f7;
    --ink: #2a2a2a;
    --body: #333333;
    --red: #c9262e;
    --red-light: #dc444b;
    --red-dark: #8e1a20;
    --black: #141414;
    --white: #ffffff;
  }
  * { box-sizing: border-box; margin: 0; padding: 0; }
  html, body { width: 1200px; height: 900px; overflow: hidden; background: var(--bg); }
  .flyer {
    position: absolute; left: 266px; top: 20px;
    width: 696px; height: 895px;
    transform: scale(0.96); transform-origin: top left;
    background: var(--paper); overflow: hidden;
    font-family: "Arimo", Arial, sans-serif; color: var(--body);
  }
  .header-art { position: absolute; left: 0; top: 0; }
  .brand-name {
    position: absolute; left: 30px; top: 52px;
    font-family: "Oswald", sans-serif; font-weight: 700;
    font-size: 30px; line-height: 1.05; color: var(--ink); letter-spacing: 0.5px;
  }
  .banner-title {
    position: absolute; left: 22px; top: 158px;
    font-family: "Anton", sans-serif; font-size: 50px; line-height: 1;
    color: var(--white); letter-spacing: 0.5px;
    text-shadow: 2px 2px 0 rgba(0,0,0,0.35);
  }
  .main-column {
    position: absolute; left: 17px; top: 255px; width: 390px;
  }
  .section-title {
    font-family: "Oswald", sans-serif; font-weight: 700; color: var(--ink);
    font-size: 23px; line-height: 1.1; text-transform: uppercase;
  }
  .section-title.why { font-size: 20.5px; }
  .sub-title {
    font-family: "Oswald", sans-serif; font-weight: 700; color: var(--ink);
    font-size: 17px; line-height: 1.2; margin-top: 2px; text-transform: uppercase;
  }
  .main-column p { font-size: 13.4px; line-height: 16.3px; margin: 4px 0 6px; }
  .resource-list { list-style: none; margin: 6px 0 4px 4px; }
  .resource-list li {
    position: relative; padding-left: 12px; font-size: 13.4px; line-height: 16.3px; margin-bottom: 3px;
  }
  .resource-list li::before {
    content: ""; position: absolute; left: 0; top: 6px; width: 5px; height: 5px;
    border-radius: 50%; background: var(--ink);
  }
  .contact-box {
    position: absolute; left: 0; top: 760px; width: 355px; height: 140px;
    background: var(--black); border-top-right-radius: 24px; color: var(--white);
    padding: 8px 0 0 32px;
  }
  .contact-title { font-weight: 700; font-size: 18.5px; letter-spacing: 0.3px; margin-bottom: 8px; }
  .contact-row { display: flex; align-items: center; gap: 12px; font-size: 16.5px; height: 30px; padding-left: 8px; }
  .contact-row svg { width: 21px; height: 21px; flex: none; }
  .side-column {
    position: absolute; left: 408px; top: 243px; width: 261px; height: 652px;
    background: var(--red); color: var(--white); padding: 4px 6px 0 7px;
  }
  .side-title {
    font-family: "Oswald", sans-serif; font-weight: 700; font-size: 22px; line-height: 1.12;
    text-transform: uppercase;
  }
  .side-title.centered { padding-left: 5px; }
  .category-list { list-style: none; margin: 2px 0 8px 8px; }
  .category-list li {
    position: relative; padding-left: 20px; font-weight: 700; font-size: 13.3px; line-height: 18.2px;
    text-transform: uppercase;
  }
  .category-list li::before {
    content: ""; position: absolute; left: 2px; top: 7px; width: 5px; height: 5px;
    border-radius: 50%; background: var(--white);
  }
  .category-list.specialties li { line-height: 20.4px; }
  .category-list.specialties { margin-bottom: 5px; }
  .side-column p { font-size: 13px; line-height: 16px; margin: 2px 0 4px; letter-spacing: -0.1px; }
</style>
</head>
<body>
<div class="flyer">
  <svg class="header-art" width="696" height="245" viewBox="0 0 696 245" aria-hidden="true">
    <rect width="696" height="245" fill="#ffffff"/>
    <polygon points="578,0 696,0 696,245 428,245" fill="#161616"/>
    <polygon points="488,100 586,143 500,140" fill="#8e1a20"/>
    <polygon points="0,140 500,140 586,143 540,240 0,240" fill="#c9262e"/>
    <polygon points="0,140 500,140 586,143 560,166 0,166" fill="#dc444b" opacity="0.75"/>
  </svg>

  <div class="brand-name">Brightvale Parts &amp; Supply<br>Company</div>
  <div class="banner-title">SHOP AND EXPLORE PARTS</div>

  <section class="main-column">
    <h2 class="section-title why">Why Brightvale Parts &amp; Supply Company</h2>
    <p>Innovation brings challenge and opportunity, and we’re suiting up for both. Because when it comes to the evolving maintenance, repair, collision and powertrain needs of Ardell, Brennick, Stroud and Calloway vehicles, only Brightvale Parts &amp; Supply Company Original Equipment parts offer true OE Original Equipment built for what’s next. We also offer Gold and Silver parts, our high-quality OE alternatives.</p>

    <h2 class="section-title">Trade Professionals</h2>
    <h3 class="sub-title">Technical Resources</h3>
    <p>We’re preparing trade professionals to help vehicle owners with their maintenance, repair and collision needs while sustaining a successful automotive business. In our technical resources, you can find and access:</p>
    <ul class="resource-list">
      <li>Manuals and technical documents</li>
      <li>Programs designed to help accelerate trade professionals’ success</li>
      <li>Specialized trainings and educational programs</li>
      <li>Offers set up specifically to reward trade professionals</li>
    </ul>
    <h3 class="sub-title">Technical Training</h3>
    <p>Ready to take the next steps for your professional career development? We’ve compiled resources, tools and other trainings to help prepare trade professionals. Find your next move with our technical training:</p>
  </section>

  <aside class="side-column">
    <h2 class="side-title centered">Top Parts Categories</h2>
    <ul class="category-list">
      <li>Engines</li>
      <li>Filter</li>
      <li>Chemical &amp; Fluids</li>
      <li>Ignition Parts</li>
      <li>Batteries &amp; Related Parts</li>
      <li>Transmission</li>
      <li>Steering &amp; Suspension</li>
      <li>Heating &amp; Air Conditioning</li>
      <li>Tires &amp; Wheels</li>
      <li>Electrical</li>
      <li>Brake System</li>
      <li>Body</li>
    </ul>
    <h2 class="side-title">Additional Specialties</h2>
    <ul class="category-list specialties">
      <li>Maintenance</li>
      <li>Repair</li>
      <li>Collision</li>
      <li>Powertrain</li>
      <li>Ardell Performance</li>
    </ul>
    <h2 class="side-title">OE Original Equipment</h2>
    <p>Brightvale Original Equipment parts are built on innovation that never lets up. When you choose a true OE part designed, engineered, tested and backed by OE for your vehicle, you’re making the right choice.</p>
    <h2 class="side-title">Aftermarket</h2>
    <p>Brightvale offers the only aftermarket parts backed by its Gold and Silver lines of premium parts that offer a precise fit for Halbrook vehicles and most other makes and models.</p>
  </aside>

  <footer class="contact-box">
    <div class="contact-title">CONTACT US FOR MORE INFO</div>
    <div class="contact-row">
      <svg viewBox="0 0 24 24" aria-hidden="true"><path fill="#fff" d="M6.6 10.8c1.4 2.8 3.8 5.1 6.6 6.6l2.2-2.2c.3-.3.7-.4 1-.2 1.1.4 2.3.6 3.6.6.6 0 1 .4 1 1V20c0 .6-.4 1-1 1C10.6 21 3 13.4 3 4c0-.6.4-1 1-1h3.5c.6 0 1 .4 1 1 0 1.3.2 2.5.6 3.6.1.3 0 .7-.2 1z"/></svg>
      <span>555-014-0199</span>
    </div>
    <div class="contact-row">
      <svg viewBox="0 0 24 24" aria-hidden="true"><rect x="2.5" y="5" width="19" height="14" fill="none" stroke="#fff" stroke-width="2"/><path d="M3 6l9 7 9-7" fill="none" stroke="#fff" stroke-width="2"/></svg>
      <span>www.brightvaleparts.com</span>
    </div>
    <div class="contact-row">
      <svg viewBox="0 0 24 24" aria-hidden="true"><g fill="none" stroke="#fff" stroke-width="1.8"><circle cx="12" cy="12" r="9.5"/><ellipse cx="12" cy="12" rx="4" ry="9.5"/><path d="M2.5 12h19M4 7h16M4 17h16"/></g></svg>
      <span>www.brightvaleparts.com</span>
    </div>
  </footer>
</div>
</body>
</html>
```